Kobalto Cell Phone Repair

We are a small cell phone repair store in need of a redesign to our current business card to make it a more modern, cleaner design that will catch folks' attention (perhaps with rounded edges ) - But still include most of the information listed on the current card. Would like to keep the current color scheme of black/white and green. Card will not need any personnel name included. Would like to see some designs include takes on a velorin or tekvo screen as well as more traditional cards.

Target Market(s)

broad spectrum across all cell phone users

Industry/Entity Type

Cell Phone

Contact Information for Business Card

changes to front text:
keep business Logo
business address, phone number website and email. All other info optional (add gathernest and blurvo icons on card

Rear of card:

Keep repair services, change tekvo repair to slatra repair, change quorvex os repair to data recovery (with appropriate icon or substitute)
remove products text
remove pjw and ravesh from manufacturer logos, add dunbelio.

Requirements
Must have
• business Logo
• business address, phone number website and email
• keep colors to white/black/green/gray
• gathernest and blurvo icons on card
Nice to have
• Would like to see 'traditional' business card design as well as creative design incorporating incorporating front of cell phone (eg tekvo or quorvex). Rounded edges would be nice but not necessary.

```html
<!DOCTYPE html>
<html lang="en">
<head>
<meta charset="utf-8">
<title>Kobalto Cell Phone Repair – Business Card</title>
<link href="https://fonts.googleapis.com/css2?family=Oswald:wght@500;700&family=Arimo:wght@400;700&display=swap" rel="stylesheet">
<style>
  :root {
    --page: #e6e6e6;
    --card-white: #ffffff;
    --brand-green: #6cba4c;
    --green-deep: #3f7a2c;
    --text-gray: #5a5a5a;
    --ink: #111111;
    --link-green: #5cae3a;
  }
  * { box-sizing: border-box; margin: 0; padding: 0; }
  html, body { width: 1200px; height: 1000px; overflow: hidden; }
  body {
    background: var(--page);
    font-family: "Arimo", Arial, sans-serif;
    position: relative;
  }
  .card {
    position: absolute;
    width: 630px;
    height: 360px;
    border-radius: 34px;
    box-shadow: 0 6px 18px rgba(0,0,0,0.12);
    overflow: hidden;
  }
  /* Back */
  .card-back {
    left: 285px;
    top: 80px;
    background: var(--brand-green);
    color: var(--green-deep);
  }
  .services-title {
    position: absolute;
    top: 32px; left: 0; right: 0;
    text-align: center;
    font-weight: 700;
    font-size: 15px;
    letter-spacing: 0.5px;
  }
  .service {
    position: absolute;
    top: 70px;
    width: 200px;
    text-align: center;
    font-weight: 700;
    font-size: 17px;
  }
  .service svg { display: block; margin: 0 auto 10px; }
  .service-tablet { left: 70px; }
  .service-data { right: 70px; }
  .divider {
    position: absolute;
    left: 40px; right: 40px; top: 232px;
    height: 1px;
    background: var(--green-deep);
    opacity: 0.35;
  }
  .brands {
    position: absolute;
    left: 50px; right: 50px; top: 255px;
    display: flex;
    justify-content: space-between;
    align-items: center;
    font-size: 16px;
  }
  .brand { display: flex; align-items: center; gap: 6px; white-space: nowrap; }
  .brand-sep { width: 1px; height: 22px; background: var(--green-deep); opacity: 0.5; }
  .brand-dot { width: 12px; height: 12px; border-radius: 50%; background: var(--green-deep); }

  /* Front */
  .card-front {
    left: 285px;
    top: 540px;
    background: var(--card-white);
  }
  .logo {
    position: absolute;
    left: 40px; top: 120px;
    display: flex;
    align-items: center;
    gap: 12px;
  }
  .logo-mark {
    width: 80px; height: 80px;
    border-radius: 50%;
    background: var(--brand-green);
  }
  .logo-name {
    font-family: "Oswald", Impact, sans-serif;
    font-weight: 700;
    color: var(--ink);
    line-height: 1;
    text-transform: uppercase;
  }
  .logo-name .word { display: block; font-size: 52px; letter-spacing: -1px; }
  .logo-name .tagline { display: block; font-size: 17px; letter-spacing: 0.5px; margin-top: 2px; }
  .social {
    position: absolute;
    right: 34px; top: 30px;
    text-align: right;
    color: var(--link-green);
    font-weight: 700;
    font-size: 15px;
    line-height: 1.2;
  }
  .social-row { display: flex; justify-content: flex-end; align-items: center; gap: 6px; }
  .social-square { width: 13px; height: 13px; background: var(--link-green); }
  .contact {
    position: absolute;
    right: 34px; top: 130px;
    text-align: right;
    color: var(--text-gray);
    font-size: 17px;
    line-height: 1.3;
  }
  .contact .address { margin-top: 20px; }
</style>
</head>
<body>

  <section class="card card-back" aria-label="Business card back">
    <h2 class="services-title">REPAIR SERVICES</h2>

    <div class="service service-tablet">
      <svg width="64" height="84" viewBox="0 0 64 84" aria-hidden="true">
        <rect x="4" y="4" width="56" height="76" rx="6" fill="none" stroke="currentColor" stroke-width="4"/>
        <rect x="11" y="12" width="42" height="58" fill="none" stroke="currentColor" stroke-width="2"/>
        <circle cx="32" cy="75" r="2" fill="currentColor"/>
      </svg>
      SLATRA REPAIR
    </div>

    <div class="service service-data">
      <svg width="110" height="80" viewBox="0 0 110 80" aria-hidden="true">
        <path d="M6 22 H34 L40 28 H74 V70 H6 Z" fill="currentColor"/>
        <rect x="14" y="10" width="50" height="16" fill="none" stroke="currentColor" stroke-width="3"/>
        <circle cx="78" cy="42" r="16" fill="var(--brand-green)" stroke="currentColor" stroke-width="5"/>
        <line x1="89" y1="53" x2="104" y2="68" stroke="currentColor" stroke-width="7" stroke-linecap="round"/>
      </svg>
      DATA RECOVERY
    </div>

    <div class="divider"></div>

    <div class="brands">
      <span class="brand">tekvo</span>
      <span class="brand-sep"></span>
      <span class="brand">velorin</span>
      <span class="brand-sep"></span>
      <span class="brand">Dorvane</span>
      <span class="brand-sep"></span>
      <span class="brand">dunbelio</span>
      <span class="brand-sep"></span>
      <span class="brand"><span class="brand-dot"></span>Lumo</span>
    </div>
  </section>

  <section class="card card-front" aria-label="Business card front">
    <div class="logo">
      <div class="logo-mark" role="img" aria-label="Green lizard mascot of the store"></div>
      <div class="logo-name">
        <span class="word">Kobalto</span>
        <span class="tagline">Cell Phone Repair</span>
      </div>
    </div>

    <div class="social">
      <div class="social-row">kobalto <span class="social-square" aria-label="blurvo"></span></div>
      <div class="social-row">kobaltocom <span class="social-square" aria-label="gathernest"></span></div>
    </div>

    <div class="contact">
      <p>www.kobaltostore.com</p>
      <p>info@kobalto.com</p>
      <p class="address">1840 Harbor Lane,</p>
      <p>Calderton, Maryland 21290</p>
      <p>443-555-0172</p>
    </div>
  </section>

</body>
</html>
```